Trading journal (Ledger Lens)

I need a design for trading journal application.
I would like to start from dark version of the design and the main goal that it should be pretty intuitive for everyone. I am going to create the app from scratch and I don't have any logo or branding colors, so it is up to you to choose a color scheme but it is a dark mode, so one of the colors would be black obviously.
The app will be available for web PC, Android and iOS.

There is google document with the requirements.
https://files.brimvault.example/doc/7KpTzR2wQx9LmNc4VbHs8JdYf3GaUe6Wo1XiRq5Zt0Ay/view?mode=share

Target Market(s)

Professional traders

Industry/Entity Type

Trading

Colors

Designer to choose colors to be used in the design.

Requirements
Must have
• Dark mode design for PC and mobile views, the design must be pretty intuitive for everyone.
Nice to have
• Tooltips for something non obvious; popovers after completing some actions

```html
<!DOCTYPE html>
<html lang="en">
<head>
<meta charset="utf-8">
<title>Ledger Lens – Add Trade</title>
<link href="https://fonts.googleapis.com/css2?family=Poppins:ital,wght@0,400;0,500;0,600;1,400&display=swap" rel="stylesheet">
<style>
:root{
  --board-top:#0d5670;
  --board-bottom:#137a4c;
  --screen:#111315;
  --panel:#1a1c1f;
  --card:#202327;
  --card-body:#17191c;
  --field:#0f1113;
  --line:#2c3035;
  --text:#f1f3f5;
  --muted:#9aa0a8;
  --green:#1fd58c;
  --red:#f0544f;
  --accent:linear-gradient(90deg,#1a8ee6,#1ed79a);
}
*{box-sizing:border-box;margin:0;padding:0}
html,body{width:965px;height:1200px;overflow:hidden}
body{background:linear-gradient(180deg,#1281ad,#19b377);font-family:"Poppins",sans-serif;color:var(--text);position:relative}
.board{position:absolute;left:15px;top:15px;width:935px;height:1170px;border-radius:20px;background:linear-gradient(180deg,var(--board-top),var(--board-bottom))}
.screen{position:absolute;left:121px;width:724px;background:var(--screen);border-radius:12px;overflow:hidden}
.screen--main{top:65px;height:565px}
.screen--modal{top:670px;height:402px}
.abs{position:absolute}
.menu-icon{left:16px;top:13px}
.brand{left:34px;top:10px;display:flex;align-items:center;gap:5px;font-size:8.5px;font-weight:500;color:var(--green)}
.brand-mark{width:14px;height:14px;border:1.2px solid var(--green);border-radius:4px}
.greeting{left:141px;top:14px;font-size:7.5px}
.search{left:223px;top:8px;width:180px;height:23px;border:1px solid var(--line);border-radius:6px;font-size:6px;color:var(--muted);padding:0 8px;display:flex;align-items:center;justify-content:space-between}
.account{left:543px;top:8px;width:92px;height:24px;background:#1a1c1f;border-radius:6px;display:flex;align-items:center;gap:5px;padding:0 8px;font-size:6px;font-weight:500}
.account .caret{margin-left:auto}
.bell{left:650px;top:12px}
.bell-badge{left:658px;top:10px;width:8px;height:8px;border-radius:50%;background:var(--green);color:#0b0c0d;font-size:4.5px;font-weight:600;display:flex;align-items:center;justify-content:center}
.avatar{left:681px;top:9px;width:21px;height:21px;border-radius:50%;background:linear-gradient(135deg,#7d8a99,#3b4756)}
.import-btn{left:8px;top:45px;width:110px;height:25px;border-radius:6px;background:var(--accent);display:flex;align-items:center;justify-content:center;gap:5px;font-size:7.5px;font-weight:500}
.nav-item{left:8px;width:110px;height:25px;border-radius:6px;display:flex;align-items:center;gap:7px;padding-left:8px;font-size:6.5px;color:#d8dce0}
.nav-item.is-active{background:#1c1f22;color:var(--green)}
.panel{left:135px;top:44px;width:568px;height:500px;background:var(--panel);border:1px solid #23262a;border-radius:10px}
.page-title{left:16px;top:12px;font-size:12.5px;font-weight:600}
.page-sub{left:16px;top:30px;font-size:5.5px;color:var(--muted);display:flex;align-items:center;gap:4px}
.btn{height:20px;width:64px;border-radius:11px;display:flex;align-items:center;justify-content:center;gap:5px;font-size:7px;font-weight:500}
.btn--ghost{border:1px solid #d9dce0}
.btn--primary{background:var(--accent)}
.field-label{font-size:5.8px;color:#cfd3d8}
.field{height:20px;background:var(--field);border-radius:4px;display:flex;align-items:center;padding:0 8px;font-size:6.5px;font-weight:500}
.field .hint{color:#555b63;font-size:5px;font-weight:400;margin-left:2px}
.cursor{width:1px;height:9px;background:var(--green);display:inline-block;margin:0 1px}
.field .trail{margin-left:auto}
.exec{left:14px;width:539px;height:160px;background:var(--card);border-radius:8px}
.exec-title{left:10px;top:10px;font-size:7.5px;font-weight:500}
.exec-actions{right:10px;top:10px;display:flex;align-items:center;gap:8px;font-size:6px;font-weight:500}
.exec-actions .del{color:var(--red);display:flex;gap:4px;align-items:center}
.exec-actions .edit{color:var(--green);display:flex;gap:4px;align-items:center}
.exec-actions .sep{width:1px;height:8px;background:var(--line)}
.exec-body{left:2px;top:26px;width:535px;height:132px;background:var(--card-body);border-radius:7px}
.data-col{top:8px}
.data-row{display:flex;height:12.1px;align-items:center}
.data-row dt{font-size:5px;color:var(--muted);text-transform:uppercase}
.data-row dd{font-size:6.3px;font-weight:600}
.col-a{left:7px}.col-a dt{width:74px}
.col-b{left:187px}.col-b dt{width:53px}
.divider{left:306px;top:10px;width:1px;height:114px;background:var(--line)}
.col-c{left:326px;top:8px;width:205px}
.meta-label{font-size:5px;color:var(--muted);margin-bottom:4px}
.chips{display:flex;gap:3px;margin-bottom:9px}
.chip{height:9px;padding:0 3px;border-radius:2px;font-size:4.5px;font-weight:600;display:flex;align-items:center}
.chip--blue{background:#e8f2ff;color:#1565d8}
.chip--orange{background:#fff1e3;color:#e3620f}
.chip--purple{background:#f0e9ff;color:#6b2fd6}
.chip--green{background:#e6fbef;color:#119b4b}
.note{font-size:6px;font-style:italic;line-height:8.5px}
.add-exec{left:16px;top:468px;width:100px;height:16px;border:1px solid var(--green);border-radius:9px;color:var(--green);font-size:6px;font-weight:500;display:flex;align-items:center;justify-content:center;gap:4px}
.scrim{inset:0;background:rgba(8,9,10,.82)}
.modal{left:236px;top:26px;width:251px;height:351px;background:#1a1c1f;border:1px solid #2a2d31;border-radius:10px}
.modal-title{left:15px;top:17px;font-size:10.5px;font-weight:600}
.modal-scroll{left:15px;top:50px;width:220px;height:258px;overflow:hidden}
.m-label{position:absolute;left:0;font-size:5.8px;color:#cfd3d8}
.m-field{position:absolute;left:0;width:219px;height:20px;background:var(--field);border-radius:4px;display:flex;align-items:center;justify-content:space-between;padding:0 7px;font-size:6.3px;font-weight:500}
.segment{position:absolute;left:0;width:219px;height:20px;background:var(--field);border-radius:4px;display:flex;padding:2px;gap:2px}
.segment span{flex:1;display:flex;align-items:center;justify-content:center;font-size:4.8px;font-weight:600;border-radius:3px}
.segment .is-on{background:#24272b;color:var(--green)}
.modal-btn{top:320px;width:101px;height:20px;border-radius:11px;display:flex;align-items:center;justify-content:center;gap:5px;font-size:7px;font-weight:500}
</style>
</head>
<body>
<div class="board"></div>

<section class="screen screen--main">
  <svg class="abs menu-icon" width="10" height="8" viewBox="0 0 10 8"><path d="M1 1h8M1 4h8M1 7h8" stroke="#d8dce0" stroke-width="1" stroke-linecap="round"/></svg>
  <div class="abs brand"><span class="brand-mark"></span>Ledger Lens</div>
  <div class="abs greeting">Good day, Marlo!</div>
  <div class="abs search">Search<svg width="7" height="7" viewBox="0 0 10 10"><circle cx="4.3" cy="4.3" r="3.3" fill="none" stroke="#9aa0a8" stroke-width="1.2"/><path d="M6.8 6.8 9 9" stroke="#9aa0a8" stroke-width="1.2"/></svg></div>
  <div class="abs account"><svg width="10" height="9" viewBox="0 0 10 9"><rect x=".6" y="1.5" width="8.8" height="7" rx="1.5" fill="none" stroke="#1a8ee6"/><path d="M6.5 5h3" stroke="#1ed79a"/></svg>LX #Q731902...<svg class="caret" width="6" height="4" viewBox="0 0 6 4"><path d="M1 1l2 2 2-2" stroke="#1fd58c" fill="none"/></svg></div>
  <svg class="abs bell" width="11" height="12" viewBox="0 0 11 12"><path d="M2 8.5V5a3.5 3.5 0 0 1 7 0v3.5l1 1H1z M4.3 10.8h2.4" fill="none" stroke="#9aa0a8" stroke-width="1"/></svg>
  <div class="abs bell-badge">4</div>
  <div class="abs avatar" role="img" aria-label="User profile photo"></div>

  <div class="abs import-btn"><svg width="10" height="10" viewBox="0 0 10 10"><path d="M5 1a4 4 0 1 0 4 4M5 1v4h4" fill="none" stroke="#fff" stroke-width="1"/></svg>Import</div>
  <div class="abs nav-item" style="top:82px"><svg width="10" height="10" viewBox="0 0 10 10"><rect x=".5" y=".5" width="9" height="9" rx="2" fill="none" stroke="#cfd3d8"/><path d="M4 .5v9M4 5h5.5" stroke="#cfd3d8"/></svg>Dashboard</div>
  <div class="abs nav-item is-active" style="top:109px"><svg width="10" height="10" viewBox="0 0 10 10"><rect x=".5" y=".5" width="9" height="9" rx="2" fill="none" stroke="#1fd58c"/><path d="M3 7V5M5 7V4M7 7V3" stroke="#1fd58c"/></svg>Trade</div>
  <div class="abs nav-item" style="top:136px"><svg width="10" height="10" viewBox="0 0 10 10"><rect x=".5" y="1.5" width="9" height="8" rx="2" fill="none" stroke="#cfd3d8"/><path d="M.5 4h9M3 .5v2M7 .5v2" stroke="#cfd3d8"/></svg>Calendar</div>
  <div class="abs nav-item" style="top:163px"><svg width="10" height="10" viewBox="0 0 10 10"><path d="M5 .6 9 2.8v4.4L5 9.4 1 7.2V2.8z" fill="none" stroke="#cfd3d8"/><circle cx="5" cy="5" r="1.5" fill="none" stroke="#cfd3d8"/></svg>Settings</div>
  <div class="abs nav-item" style="top:190px"><svg width="10" height="10" viewBox="0 0 10 10"><rect x=".5" y=".5" width="9" height="9" rx="2" fill="none" stroke="#cfd3d8"/><circle cx="5" cy="4" r="1.6" fill="none" stroke="#cfd3d8"/><path d="M2.5 8.5a2.6 2.6 0 0 1 5 0" fill="none" stroke="#cfd3d8"/></svg>My Account</div>

  <div class="abs panel">
    <h1 class="abs page-title">Add Trade</h1>
    <div class="abs page-sub"><svg width="7" height="7" viewBox="0 0 7 7"><circle cx="3.5" cy="3.5" r="3.5" fill="#6d737b"/><path d="M3.5 3v2" stroke="#1a1c1f"/></svg>Use your account time zone (GMT +01:00)</div>
    <div class="abs btn btn--ghost" style="left:412px;top:17px"><svg width="6" height="6" viewBox="0 0 6 6"><path d="M1 1l4 4M5 1 1 5" stroke="#fff"/></svg>Cancel</div>
    <div class="abs btn btn--primary" style="left:488px;top:17px"><svg width="9" height="9" viewBox="0 0 9 9"><circle cx="4.5" cy="4.5" r="3.8" fill="none" stroke="#fff" stroke-width=".9"/><path d="M2.8 4.6l1.2 1.1 2.2-2.3" fill="none" stroke="#fff" stroke-width=".9"/></svg>Confirm</div>

    <div class="abs field-label" style="left:16px;top:60px">TYPE</div>
    <div class="abs field" style="left:16px;top:72px;width:141px">Option<svg class="trail" width="6" height="4" viewBox="0 0 6 4"><path d="M1 1l2 2 2-2" stroke="#cfd3d8" fill="none"/></svg></div>
    <div class="abs field-label" style="left:182px;top:60px">UNDERLYING SYMBOL</div>
    <div class="abs field" style="left:182px;top:72px;width:141px">QR<span class="cursor"></span>ZX<span class="hint">(click Tab to to autocomplete)</span></div>

    <div class="abs field-label" style="left:16px;top:119px">EXECUTIONS</div>

    <article class="abs exec" style="top:133px">
      <h2 class="abs exec-title">01 - Execution</h2>
      <div class="abs exec-actions"><span class="del"><svg width="7" height="7" viewBox="0 0 7 7"><path d="M1 1.8h5M2.5 1.8V.8h2v1M1.6 1.8l.4 4.7h3l.4-4.7" fill="none" stroke="#f0544f" stroke-width=".7"/></svg>Delete</span><span class="sep"></span><span class="edit"><svg width="7" height="7" viewBox="0 0 7 7"><path d="M3 1H1v5h5V4M2.8 4.2 6 1" fill="none" stroke="#1fd58c" stroke-width=".7"/></svg>Edit</span></div>
      <div class="abs exec-body">
        <dl class="abs data-col col-a">
          <div class="data-row"><dt>Entry date</dt><dd>Jan/18/2024</dd></div>
          <div class="data-row"><dt>Entry time</dt><dd>12:48:07</dd></div>
          <div class="data-row"><dt>Type</dt><dd>Buy</dd></div>
          <div class="data-row"><dt>Direction</dt><dd>Call</dd></div>
          <div class="data-row"><dt>Expiration date</dt><dd>Jan/20/2024</dd></div>
          <div class="data-row"><dt>Strike</dt><dd>$100</dd></div>
          <div class="data-row"><dt>Contracts/shares</dt><dd>126</dd></div>
          <div class="data-row"><dt>Price</dt><dd>$12</dd></div>
          <div class="data-row"><dt>Commission</dt><dd>$7.50</dd></div>
          <div class="data-row"><dt>Fee</dt><dd>$5.40</dd></div>
        </dl>
        <dl class="abs data-col col-b">
          <div class="data-row"><dt>Stop loss</dt><dd>$90</dd></div>
          <div class="data-row"><dt>Take profit</dt><dd>$180</dd></div>
          <div class="data-row"><dt>Risk</dt><dd>$150</dd></div>
          <div class="data-row"><dt>Exit price</dt><dd>$15.00</dd></div>
          <div class="data-row"><dt>Exit date</dt><dd>Jan/21/2024</dd></div>
          <div class="data-row"><dt>Exit time</dt><dd>12:47.00</dd></div>
        </dl>
        <div class="abs divider"></div>
        <div class="abs col-c">
          <div class="meta-label">STRATEGY</div>
          <div class="chips"><span class="chip chip--blue">BREAKOUT</span><span class="chip chip--blue">SAMPLE TAG</span><span class="chip chip--orange">BUY DIP</span></div>
          <div class="meta-label">TAGS</div>
          <div class="chips"><span class="chip chip--purple">GAP AND GO</span><span class="chip chip--blue">VOLUME GAINER</span><span class="chip chip--green">CONTACT WINNER</span><span class="chip chip--orange">CHASED</span></div>
          <div class="meta-label">MOOD</div>
          <div class="chips"><span class="chip chip--orange">SAMPLE ONE</span><span class="chip chip--orange">MOOD 2</span></div>
          <div class="meta-label">NOTES</div>
          <p class="note">Lorem ipsum dolor sit amet consectetur. Donec at pellentesque amet mattis.</p>
        </div>
      </div>
    </article>

    <article class="abs exec" style="top:300px">
      <h2 class="abs exec-title">02 - Execution</h2>
      <div class="abs exec-actions"><span class="del"><svg width="7" height="7" viewBox="0 0 7 7"><path d="M1 1.8h5M2.5 1.8V.8h2v1M1.6 1.8l.4 4.7h3l.4-4.7" fill="none" stroke="#f0544f" stroke-width=".7"/></svg>Delete</span><span class="sep"></span><span class="edit"><svg width="7" height="7" viewBox="0 0 7 7"><path d="M3 1H1v5h5V4M2.8 4.2 6 1" fill="none" stroke="#1fd58c" stroke-width=".7"/></svg>Edit</span></div>
      <div class="abs exec-body">
        <dl class="abs data-col col-a">
          <div class="data-row"><dt>Entry date</dt><dd>Jan/18/2024</dd></div>
          <div class="data-row"><dt>Entry time</dt><dd>12:48:07</dd></div>
          <div class="data-row"><dt>Type</dt><dd>Buy</dd></div>
          <div class="data-row"><dt>Direction</dt><dd>Call</dd></div>
          <div class="data-row"><dt>Expiration date</dt><dd>Jan/20/2024</dd></div>
          <div class="data-row"><dt>Strike</dt><dd>$100</dd></div>
          <div class="data-row"><dt>Contracts/shares</dt><dd>126</dd></div>
          <div class="data-row"><dt>Price</dt><dd>$12</dd></div>
          <div class="data-row"><dt>Commission</dt><dd>$7.50</dd></div>
          <div class="data-row"><dt>Fee</dt><dd>$5.40</dd></div>
        </dl>
        <dl class="abs data-col col-b">
          <div class="data-row"><dt>Stop loss</dt><dd>$90</dd></div>
          <div class="data-row"><dt>Take profit</dt><dd>$180</dd></div>
          <div class="data-row"><dt>Risk</dt><dd>$150</dd></div>
          <div class="data-row"><dt>Exit price</dt><dd>$15.00</dd></div>
          <div class="data-row"><dt>Exit date</dt><dd>Jan/21/2024</dd></div>
          <div class="data-row"><dt>Exit time</dt><dd>12:47.00</dd></div>
        </dl>
        <div class="abs divider"></div>
        <div class="abs col-c">
          <div class="meta-label">STRATEGY</div>
          <div class="chips"><span class="chip chip--blue">SAMPLE TAG</span><span class="chip chip--orange">BUY DIP</span></div>
          <div class="meta-label">TAGS</div>
          <div class="chips"><span class="chip chip--green">CONTACT WINNER</span><span class="chip chip--purple">GAP AND GO</span><span class="chip chip--orange">CHASED</span></div>
          <div class="meta-label">MOOD</div>
          <div class="chips"><span class="chip chip--orange">SECOND MODE</span></div>
          <div class="meta-label">NOTES</div>
          <p class="note">Sit odio adipiscing elementum maecenas. Etiam at dui sit vitae mauris mollis adipiscing non. Est id nibh elit feugiat tellus diam.</p>
        </div>
      </div>
    </article>

    <div class="abs add-exec"><svg width="6" height="6" viewBox="0 0 6 6"><path d="M3 .5v5M.5 3h5" stroke="#1fd58c"/></svg>Add another exectution</div>
  </div>
</section>

<section class="screen screen--modal">
  <svg class="abs menu-icon" width="10" height="8" viewBox="0 0 10 8"><path d="M1 1h8M1 4h8M1 7h8" stroke="#d8dce0" stroke-width="1" stroke-linecap="round"/></svg>
  <div class="abs brand"><span class="brand-mark"></span>Ledger Lens</div>
  <div class="abs greeting">Good day, Marlo!</div>
  <div class="abs search">Search</div>
  <div class="abs account">LX #Q731902...</div>
  <div class="abs avatar" role="img" aria-label="User profile photo"></div>
  <div class="abs import-btn">Import</div>
  <div class="abs nav-item" style="top:82px">Dashboard</div>
  <div class="abs nav-item is-active" style="top:109px">Trade</div>
  <div class="abs nav-item" style="top:136px">Calendar</div>
  <div class="abs nav-item" style="top:163px">Settings</div>
  <div class="abs nav-item" style="top:190px">My Account</div>
  <div class="abs panel">
    <h1 class="abs page-title">Add Trade</h1>
    <div class="abs btn btn--ghost" style="left:412px;top:17px">Cancel</div>
    <div class="abs btn btn--primary" style="left:488px;top:17px">Confirm</div>
    <div class="abs field-label" style="left:16px;top:60px">TYPE</div>
    <div class="abs field" style="left:16px;top:72px;width:141px">Option</div>
    <div class="abs field-label" style="left:16px;top:119px">EXECUTIONS</div>
    <article class="abs exec" style="top:133px">
      <h2 class="abs exec-title">01 - Execution</h2>
      <div class="abs exec-body">
        <div class="abs col-c">
          <div class="meta-label">STRATEGY</div>
          <div class="chips"><span class="chip chip--blue">BREAKOUT</span><span class="chip chip--blue">SAMPLE TAG</span><span class="chip chip--orange">BUY DIP</span></div>
          <div class="meta-label">TAGS</div>
          <div class="chips"><span class="chip chip--purple">GAP AND GO</span><span class="chip chip--blue">VOLUME GAINER</span><span class="chip chip--green">CONTACT WINNER</span><span class="chip chip--orange">CHASED</span></div>
          <div class="meta-label">MOOD</div>
          <div class="chips"><span class="chip chip--orange">SAMPLE ONE</span><span class="chip chip--orange">MOOD 2</span></div>
          <div class="meta-label">NOTES</div>
          <p class="note">Lorem ipsum dolor sit amet consectetur. Donec at pellentesque amet mattis.</p>
        </div>
      </div>
    </article>
    <article class="abs exec" style="top:300px">
      <h2 class="abs exec-title">02 - Execution</h2>
    </article>
  </div>
  <div class="abs scrim"></div>

  <div class="abs modal" role="dialog" aria-label="Edit execution 1">
    <h2 class="abs modal-title">Edit execution 1</h2>
    <div class="abs modal-scroll">
      <span class="m-label" style="top:0">ENTRY DATE</span>
      <div class="m-field" style="top:8px">Jan/18/2024<svg width="8" height="8" viewBox="0 0 8 8"><rect x=".5" y="1" width="7" height="6.5" rx="1.3" fill="none" stroke="#9aa0a8" stroke-width=".7"/><path d="M.5 3h7M2.3 0v2M5.7 0v2" stroke="#9aa0a8" stroke-width=".7"/></svg></div>
      <span class="m-label" style="top:46px">ENTRY TIME</span>
      <div class="m-field" style="top:54px">12:48:07</div>
      <span class="m-label" style="top:92px">TYPE</span>
      <div class="segment" style="top:100px"><span class="is-on">BUY</span><span>SELL</span></div>
      <span class="m-label" style="top:138px">DIRECTION</span>
      <div class="segment" style="top:146.5px"><span>CALL</span><span class="is-on">PUT</span></div>
      <span class="m-label" style="top:184px">EXPIRATION DATE</span>
      <div class="m-field" style="top:193px">Jan/20/2024<svg width="8" height="8" viewBox="0 0 8 8"><rect x=".5" y="1" width="7" height="6.5" rx="1.3" fill="none" stroke="#9aa0a8" stroke-width=".7"/><path d="M.5 3h7M2.3 0v2M5.7 0v2" stroke="#9aa0a8" stroke-width=".7"/></svg></div>
      <span class="m-label" style="top:231px">STRIKE</span>
      <div class="m-field" style="top:243px;align-items:flex-start;padding-top:5px"><svg width="9" height="9" viewBox="0 0 9 9"><circle cx="4.5" cy="4.5" r="4" fill="none" stroke="#9aa0a8" stroke-width=".7"/><path d="M4.5 1.8v5.4M5.8 3.2c-.3-.5-2.6-.6-2.6.5s2.6.6 2.6 1.6-2.3 1-2.6.4" fill="none" stroke="#9aa0a8" stroke-width=".6"/></svg>100.00</div>
    </div>
    <div class="abs modal-btn btn--ghost" style="left:15px"><svg width="6" height="6" viewBox="0 0 6 6"><path d="M1 1l4 4M5 1 1 5" stroke="#fff"/></svg>Discard</div>
    <div class="abs modal-btn btn--primary" style="left:134px"><svg width="9" height="9" viewBox="0 0 9 9"><circle cx="4.5" cy="4.5" r="3.8" fill="none" stroke="#fff" stroke-width=".9"/><path d="M2.8 4.6l1.2 1.1 2.2-2.3" fill="none" stroke="#fff" stroke-width=".9"/></svg>Save</div>
  </div>
</section>
</body>
</html>
```